The Ashcombe- outdoor banner

This should be a horizontal banner. It should have the logos attached incorporated and the following details
Coming Spring 2025: The Ashcombe - Exclusive Luxury Condos
Listed by Marisol Avenell | Quillfield Realty
Construction by Pinegate Builders
Unveil the height of luxury living with The Ashcombe, a new condo building in East Boston, set for completion in Spring 2025. Experience a standard of elegance and sophistication like never before.
For more information and inquiries, please contact:
Marisol Avenell
Phone: (617) 490-7163
Email: marisol@quillfieldhomes.example
The banner should be very classy incorporting gold and navy very classic fonts. The Ashcombe should look very classy and exclusive. The pinegate builders logo should be smaller. It should not include their phone number and instagram handle only the name of the company. Herringbone pattern in the background would be great. This is going outside the building to advertise pre construction units

```html
<!DOCTYPE html>
<html lang="en">
<head>
<meta charset="utf-8">
<title>The Ashcombe – Outdoor Banner</title>
<link href="https://fonts.googleapis.com/css2?family=Great+Vibes&family=Cormorant+SC:wght@500;600&family=Libre+Baskerville:ital@1&family=Montserrat:wght@500;700&display=swap" rel="stylesheet">
<style>
  :root {
    --navy: #0f1f5c;
    --gold: #e2b05f;
    --gold-text: #f0b650;
    --white: #ffffff;
    --stage: #d4d4d4;
    --rule: rgba(226, 176, 95, 0.55);
  }
  * { box-sizing: border-box; margin: 0; padding: 0; }
  html, body {
    width: 887px; height: 1200px; overflow: hidden;
    background: radial-gradient(ellipse at center, #ececec 0%, var(--stage) 75%);
  }
  .banner {
    position: absolute; left: 23px; top: 390px;
    width: 840px; height: 420px;
    box-shadow: 0 14px 24px rgba(0,0,0,0.22);
    overflow: hidden;
  }
  .band { position: absolute; left: 0; width: 100%; }
  .band--top { top: 0; height: 132px; background: var(--navy); }
  .band--feature { top: 132px; height: 148px; background: var(--gold); }
  .band--details { top: 280px; height: 140px; background: var(--navy); }

  .brand {
    position: absolute; left: 278px; top: 27px;
    display: flex; align-items: center; gap: 12px;
  }
  .brand__dot {
    width: 78px; height: 78px; border-radius: 50%;
    border: 3px solid var(--gold-text);
  }
  .brand__name {
    font-family: "Cormorant SC", serif; font-weight: 500;
    font-size: 30px; color: var(--gold-text); letter-spacing: 1px;
  }

  .builder { position: absolute; left: 700px; top: 30px; width: 110px; text-align: center; }
  .builder__label { font-family: "Montserrat", sans-serif; font-weight: 500; font-size: 9px; color: var(--white); }
  .builder__badge {
    margin: 7px auto 0; width: 84px; height: 52px; border-radius: 6px;
    background: var(--white); display: flex; align-items: center; justify-content: center;
    font-family: "Montserrat", sans-serif; font-weight: 700; font-size: 9px;
    color: var(--navy); line-height: 1.2; padding: 0 6px;
  }

  .feature__kicker {
    position: absolute; left: 440px; top: 8px;
    font-family: "Cormorant SC", serif; font-weight: 600; font-size: 19px;
    color: var(--white); letter-spacing: 0.5px; white-space: nowrap;
  }
  .feature__title {
    position: absolute; left: 0; width: 100%; top: 34px;
    text-align: center;
    font-family: "Great Vibes", cursive; font-weight: 400; font-size: 84px; line-height: 1;
    color: var(--white); white-space: nowrap;
  }
  .feature__tagline {
    position: absolute; left: 134px; top: 120px;
    font-family: "Cormorant SC", serif; font-weight: 600; font-size: 18px; line-height: 1;
    color: var(--white); letter-spacing: 5px; white-space: nowrap;
  }

  .col { position: absolute; top: 0; height: 100%; display: flex; flex-direction: column; justify-content: center; align-items: center; text-align: center; }
  .col--listing { left: 28px; width: 236px; }
  .col--about { left: 280px; width: 294px; }
  .col--contact { left: 584px; width: 236px; }
  .divider { position: absolute; width: 1px; background: var(--rule); }
  .divider--a { left: 271px; top: 20px; height: 100px; }
  .divider--b { left: 579px; top: 20px; height: 100px; }

  .caps { font-family: "Cormorant SC", serif; font-weight: 500; color: var(--white); }
  .listing__label { font-size: 16px; }
  .listing__agent { font-family: "Cormorant SC", serif; font-weight: 600; font-size: 20px; color: var(--gold-text); margin-top: 2px; }
  .listing__rule { width: 154px; height: 1px; background: var(--rule); margin: 8px 0 6px; }
  .listing__firm { font-family: "Cormorant SC", serif; font-weight: 500; font-size: 17px; color: var(--gold-text); }

  .about__copy {
    font-family: "Libre Baskerville", serif; font-style: italic; font-size: 10.3px;
    line-height: 1.6; color: var(--white);
  }
  .about__copy em { font-style: italic; color: var(--gold-text); }

  .contact__lead { font-size: 11.5px; line-height: 1.1; }
  .contact__agent { font-family: "Cormorant SC", serif; font-weight: 600; font-size: 17px; color: var(--gold-text); margin-top: 5px; }
  .contact__phone { font-family: "Montserrat", sans-serif; font-weight: 700; font-size: 20px; color: var(--gold-text); margin-top: 1px; }
  .contact__email { font-family: "Montserrat", sans-serif; font-weight: 500; font-size: 8.6px; color: var(--gold-text); margin-top: 2px; }
</style>
</head>
<body>
  <section class="banner" aria-label="The Ashcombe outdoor banner">
    <header class="band band--top">
      <div class="brand">
        <span class="brand__dot"></span>
        <span class="brand__name">Quillfield Realty</span>
      </div>
      <div class="builder">
        <p class="builder__label">Construction by</p>
        <div class="builder__badge">Pinegate Builders</div>
      </div>
    </header>

    <div class="band band--feature">
      <p class="feature__kicker">Coming Spring 2025</p>
      <h1 class="feature__title">The Ashcombe</h1>
      <p class="feature__tagline">Exclusive Luxury Condos</p>
    </div>

    <footer class="band band--details">
      <div class="col col--listing">
        <p class="caps listing__label">Listed by</p>
        <p class="listing__agent">Marisol Avenell</p>
        <span class="listing__rule"></span>
        <p class="listing__firm">Quillfield Realty</p>
      </div>
      <span class="divider divider--a"></span>
      <div class="col col--about">
        <p class="about__copy">Unveil the height of luxury living with<br>The Ashcombe, a new condo building in<br>East Boston, set for completion in <em>Spring 2025</em>.<br>Experience a standard of elegance and<br>sophistication like never before.</p>
      </div>
      <span class="divider divider--b"></span>
      <div class="col col--contact">
        <p class="caps contact__lead">For more information<br>and inquiries, please contact</p>
        <p class="contact__agent">Marisol Avenell</p>
        <p class="contact__phone">(617) 490-7163</p>
        <p class="contact__email">marisol@quillfieldhomes.example</p>
      </div>
    </footer>
  </section>
</body>
</html>
```